Tamber Pursuit Circuit 2017 schedule poster

A poster for the schedule of our events for the year, letting people know that they can bring their car and drive it on a track. instructors are available. included different car shots from the track. these can be included or not up to the artist's discretion. celebrating over 50 years as a club.
Updates

Project Deadline Extended
Reason: Just received dates, my apologies

Target Market(s)

young adult- retiree's

Industry/Entity Type

Car Racing

Contact Information for Business Card

A small card with the dates and Marlowe Sports Car Club logo the website MSCCVELDANE.ORG is a must, if possible any of the other information that is in the must-haves.

Font styles to use
Serif

Colors
33a6d7
85cae6
3176b5
85acd3
ffffff

Requirements
Must have
• 2017 dates, Sponsors, the website "MSCCVELDANE.ORG" , it say "2017 Tamber Pursuit Circuit", and "drive your car on a track". and say where, "Pellway Basin Sports Park". Vernal Trekday March 24-26, Event #2 April 22-23, Event #3 May 20-21, Event #4 June 24-25, Brindle Ponds Ridgerun June 11-12, Event #5 July 29-30, Event #6 August 19-20, Event #7 September 9-10, Autumn Trekday October 6-8
Nice to have
• easy to read and contrast

```html
<!DOCTYPE html>
<html lang="en">
<head>
<meta charset="utf-8">
<title>2017 Tamber Pursuit Circuit – Schedule Poster</title>
<link rel="stylesheet" href="https://fonts.googleapis.com/css2?family=Playfair+Display:ital,wght@0,400;1,700&family=Barlow+Condensed:ital,wght@1,800&family=Josefin+Sans:wght@700&family=Arimo:ital,wght@1,400;1,700&family=Lobster&display=swap">
<style>
  :root {
    --navy: #1d3f86;
    --blue-deep: #22489a;
    --blue-mid: #3176b5;
    --sky: #85cae6;
    --sky-bright: #33a6d7;
    --mist: #85acd3;
    --white: #ffffff;
    --gold: #f7b731;
    --gold-line: #f2c14a;
    --ink: #1f3a6e;
    --red: #d33a3a;
  }
  * { margin: 0; padding: 0; box-sizing: border-box; }
  html, body { width: 783px; height: 1200px; overflow: hidden; background: var(--white); }
  .poster {
    position: relative; width: 783px; height: 1200px; overflow: hidden;
    background: linear-gradient(180deg, #2a5aa8 0%, var(--blue-deep) 45%, #2450a6 75%, #2a5cb8 100%);
  }
  .photo { position: absolute; }
  .photo-top {
    left: 0; top: 0; width: 783px; height: 250px;
    background: radial-gradient(ellipse at 35% 55%, rgba(133,172,211,.35), rgba(42,90,168,0) 65%);
  }
  .photo-bottom {
    left: 0; top: 880px; width: 783px; height: 320px;
    background: radial-gradient(ellipse at 50% 70%, rgba(133,202,230,.22), rgba(42,92,184,0) 70%);
  }
  .year {
    position: absolute; left: 0; top: 188px; width: 783px; text-align: center;
    font-family: "Playfair Display", serif; font-style: italic; font-weight: 700;
    font-size: 118px; line-height: 1; color: var(--sky); letter-spacing: 2px;
  }
  .flag { position: absolute; top: 245px; }
  .flag-left { left: 166px; }
  .flag-right { left: 560px; }
  .rule { position: absolute; left: 0; width: 783px; height: 2px; background: var(--gold-line); }
  .rule-a { top: 358px; } .rule-b { top: 387px; }
  .title, .subtitle, .available, .instructors {
    position: absolute; font-family: "Barlow Condensed", sans-serif; font-style: italic;
    font-weight: 800; color: var(--white); text-transform: uppercase; line-height: 1; white-space: nowrap;
  }
  .title { left: 0; top: 322px; width: 783px; text-align: center; font-size: 100px; letter-spacing: -1px; }
  .subtitle { left: 0; top: 436px; width: 783px; text-align: center; font-size: 64px; }
  .speed-lines { position: absolute; top: 452px; }
  .speed-left { left: 96px; } .speed-right { left: 500px; }
  .banner {
    position: absolute; left: 0; top: 537px; width: 783px; height: 55px; background: var(--gold);
  }
  .banner-text {
    position: absolute; left: 72px; top: 17px; white-space: nowrap;
    font-family: "Josefin Sans", sans-serif; font-weight: 700; font-size: 23px;
    letter-spacing: 1.6px; color: var(--ink); text-transform: uppercase;
  }
  .badge { position: absolute; left: 528px; width: 240px; height: 150px; }
  .badge-one { top: 505px; } .badge-two { top: 660px; }
  .schedule-bar { position: absolute; left: 30px; top: 618px; }
  .venue {
    position: absolute; left: 92px; top: 612px; white-space: nowrap;
    font-family: "Playfair Display", serif; font-weight: 400; font-size: 27px; color: var(--sky);
  }
  .events { position: absolute; left: 0; top: 0; list-style: none; }
  .events li {
    position: absolute; white-space: nowrap; font-family: "Arimo", sans-serif;
    font-style: italic; font-size: 18.5px; color: var(--white); line-height: 1;
  }
  .events .headline { font-weight: 700; }
  .celebrate {
    position: absolute; left: 60px; top: 880px; width: 320px; text-align: center; white-space: nowrap;
    transform: rotate(-10deg); transform-origin: center;
  }
  .celebrate-over {
    font-family: "Josefin Sans", sans-serif; font-weight: 700; font-size: 26px;
    color: var(--sky); letter-spacing: 1px; text-transform: uppercase;
  }
  .celebrate-years {
    font-family: "Lobster", cursive; font-size: 54px; color: var(--gold); line-height: 1.05;
  }
  .celebrate-club {
    font-family: "Josefin Sans", sans-serif; font-weight: 700; font-size: 24px;
    color: var(--sky); letter-spacing: 2px; text-transform: uppercase;
  }
  .celebrate-club::before, .celebrate-club::after {
    content: ""; display: inline-block; width: 30px; height: 3px; background: var(--mist);
    vertical-align: middle; margin: 0 8px;
  }
  .instructors { left: 430px; top: 1030px; font-size: 48px; }
  .available { left: 378px; top: 1072px; font-size: 96px; }
</style>
</head>
<body>
<main class="poster">
  <div class="photo photo-top" role="img" aria-label="Faded photo of a vintage roadster racing on track"></div>
  <div class="photo photo-bottom" role="img" aria-label="Faded photo of a sports car cornering on track"></div>

  <svg class="flag flag-left" width="66" height="66" viewBox="0 0 66 66" aria-hidden="true">
    <defs><pattern id="checkL" width="12" height="12" patternUnits="userSpaceOnUse"><rect width="12" height="12" fill="#f6e3c6"/><rect width="6" height="6" fill="#3176b5"/><rect x="6" y="6" width="6" height="6" fill="#3176b5"/></pattern></defs>
    <line x1="8" y1="64" x2="20" y2="6" stroke="#f6e3c6" stroke-width="3"/>
    <path d="M20 6 Q40 0 62 8 L54 42 Q34 34 13 40 Z" fill="url(#checkL)"/>
  </svg>
  <svg class="flag flag-right" width="66" height="66" viewBox="0 0 66 66" aria-hidden="true">
    <defs><pattern id="checkR" width="12" height="12" patternUnits="userSpaceOnUse"><rect width="12" height="12" fill="#f6e3c6"/><rect width="6" height="6" fill="#3176b5"/><rect x="6" y="6" width="6" height="6" fill="#3176b5"/></pattern></defs>
    <line x1="4" y1="64" x2="30" y2="16" stroke="#f6e3c6" stroke-width="3"/>
    <path d="M30 16 Q44 2 62 4 L60 38 Q40 34 22 34 Z" fill="url(#checkR)"/>
  </svg>

  <h1>
    <span class="year">2017</span>
    <span class="rule rule-a"></span><span class="rule rule-b"></span>
    <span class="title">Tamber Pursuit</span>
    <span class="subtitle">Circuit</span>
  </h1>

  <svg class="speed-lines speed-left" width="180" height="34" viewBox="0 0 180 34" aria-hidden="true">
    <rect x="0" y="0" width="180" height="7" fill="#f2c14a"/><rect x="20" y="13" width="160" height="7" fill="#f2c14a"/><rect x="40" y="26" width="140" height="7" fill="#f2c14a"/>
  </svg>
  <svg class="speed-lines speed-right" width="180" height="34" viewBox="0 0 180 34" aria-hidden="true">
    <rect x="0" y="0" width="180" height="7" fill="#f2c14a"/><rect x="0" y="13" width="160" height="7" fill="#f2c14a"/><rect x="0" y="26" width="140" height="7" fill="#f2c14a"/>
  </svg>

  <div class="banner"><p class="banner-text">Drive your car on a track</p></div>

  <svg class="badge badge-one" viewBox="0 0 240 150" aria-hidden="true">
    <path d="M14 52 L70 52 L70 104 L14 104 L30 78 Z" fill="#3176b5"/>
    <path d="M226 52 L170 52 L170 104 L226 104 L210 78 Z" fill="#3176b5"/>
    <circle cx="120" cy="75" r="72" fill="#f7b731"/>
    <circle cx="120" cy="75" r="62" fill="#7da05a" role="img" aria-label="Photo of a sports car on a track"/>
    <circle cx="120" cy="75" r="50" fill="none" stroke="#ffffff" stroke-width="1.5" opacity=".8"/>
  </svg>
  <svg class="badge badge-two" viewBox="0 0 240 150" aria-hidden="true">
    <path d="M14 52 L70 52 L70 104 L14 104 L30 78 Z" fill="#3176b5"/>
    <path d="M226 52 L170 52 L170 104 L226 104 L210 78 Z" fill="#3176b5"/>
    <circle cx="120" cy="75" r="72" fill="#f7b731"/>
    <circle cx="120" cy="75" r="62" fill="#6fae4a" role="img" aria-label="Photo of a red hatchback rounding a cone"/>
    <circle cx="120" cy="75" r="50" fill="none" stroke="#ffffff" stroke-width="1.5" opacity=".8"/>
  </svg>

  <svg class="schedule-bar" width="60" height="222" viewBox="0 0 60 222" aria-hidden="true">
    <polygon points="38,0 56,0 20,222 2,222" fill="#d33a3a"/>
  </svg>

  <section class="schedule">
    <h2 class="venue">Pellway Basin Sports Park</h2>
    <ul class="events">
      <li class="headline" style="left:86px;top:651px">Vernal Trekday March 24-26</li>
      <li style="left:80px;top:671px">Event #2 April 22-23</li>
      <li style="left:76px;top:691px">Event #3 May 20-21</li>
      <li style="left:72px;top:711px">Event #4 June 24-25</li>
      <li class="headline" style="left:68px;top:736px">Brindle Ponds Ridgerun June 11-12</li>
      <li style="left:65px;top:756px">Event #5 July 29-30</li>
      <li style="left:61px;top:776px">Event #6 August 19-20</li>
      <li style="left:58px;top:796px">Event #7 September 9-10</li>
      <li class="headline" style="left:53px;top:821px">Autumn Trekday October 6-8</li>
    </ul>
  </section>

  <div class="celebrate">
    <p class="celebrate-over">Celebrating over</p>
    <p class="celebrate-years">50 years</p>
    <p class="celebrate-club">as a club</p>
  </div>

  <p class="instructors">Instructors are</p>
  <p class="available">Available</p>
</main>
</body>
</html>
```